MODERN + COOL Business Card Needed!

SUMMARY
This is for a 40+ year old family business that is transitioning to the 2nd generation and is in real need of a more modern facelift. Ive attached a company logo (I made quickly as an idea with my limited PSD skills) to start off with that you are welcome to change and draw ideas from. Ive also attached some screen shots of cards I like to give you an idea of my preferences.

WHAT WE DO
The company name is Tall Pine HK Ltd. But I prefer to just call it Tall Pine or Tall Pine with Hong Kong as kind of a sub heading on the business card. We own a factory as well as help our customers find factories to make their product. Product I mean, toys 99.9% of the time. Simple old school toys like board games, puzzles, wooden toys, baby/infant toys.

You can say we are a "sourcing" or "trading" or "consulting" company with a factory to help you do it. But since we deal with toys, i like to keep it modern and cool and fun, not serious like managing hedge funds.

WHAT WE ARE LOOKING FOR
A cool, unique looking business card that stands out. In terms of design, something modern and professional. I like darker colored cards and I like colors such as blue/green/dark gray, but am open to other colored themes. I Like bright lime green with gray, always though thats a nice combo. I prefer cards that are all colored and not so much white showing (I think). Ive attached a few screenshots of cards so take a look to get a feel of what I like.

We do alot of wooden stacking games in variety of colors too like Tovra, Lumo, Towerplix (google these to check them out). So designs that sort of resemble stacking or building would be cool but totally not necessary.

In terms of the physical aspects of the card, Im looking for a card a bit different than the standard rectangular shape. Double sided. Little things like having corner(s) be round or different angle instead of square edge I always thought was nice. Its got to be mostly a normal card size, no folding or smaller cards that fit weird in your wallet. No vertical designs. Am open to VERY different/creative shapes (as long as it still fits in a wallet good like a normal buisness card.
Updates

Hi everyone!

Just wanted to write a message to everyone to let them know all submissions are being reviewed or have been reviewed.  If I have not responded with feedback, rest assure your submission was definitely looked at in detail but I either have just been too busy to respond (alot of submissions!), or its on my to be considered list.

I respect and really enjoy receiving everyones creativity and work so I dont want it to go unrecognized - thus this message!  Feel free to submit more ideas if you like until this project ends.  Sometimes some designs just dont click but sometimes they can so you never know!

Thanks again for everyones participation and great work!

~Dev Orr

Target Market(s)

The cards are mainly handed to toy company sourcers and buyers. People I talk to ... say Pelvane for example... might want to make their next edition of Farthingale game with a reputable factory at a good cost so they can sell it to stores at a profit.

So these are the types of people I often try to talk and introduce myself and my company to.

Industry/Entity Type

Building

Colors
acd036
0392cd
00a88e
474747
606060

Requirements
Must have
• Just double sided, not plain rectangle corners, and just cool to look at and catches your eye!

Oh and the obvious business card stuff like place for name, address, number, email, etc.
Nice to have
• Think more modern and fun, not serious and old fashion (thats what we used to be!). Can use the logo I attached and you can definitely alter and change the logo or make a whole new one!

Oh and can definitely use a creative slogan if you like to think of one based on what I described in what we do.
Should not have
• Dont use fonts or text placement that might make "Tall Pine" look like "Tal Lpine"... We arent selling news papers!!

Please nothing related to education since we have the word Pine in the title, thats not our business at all.

Logo and design should not be too heavy on things related to toys, as though thats what we primarily focus on now, what we do may change over time.

```html
<!DOCTYPE html>
<html lang="en">
<head>
<meta charset="utf-8">
<title>Tall Pine Hong Kong – Business Card</title>
<link rel="stylesheet" href="https://fonts.googleapis.com/css2?family=Arimo:wght@400;700&display=swap">
<style>
  :root {
    --lime: #acd036;
    --blue: #1a94d2;
    --gray: #606060;
    --white: #ffffff;
    --backdrop: #e8e5e0;
  }
  * { margin: 0; padding: 0; box-sizing: border-box; }
  html, body { width: 1200px; height: 750px; overflow: hidden; }
  body {
    background: var(--backdrop);
    font-family: "Arimo", Arial, sans-serif;
    position: relative;
  }
  .card {
    position: absolute;
    top: 232px;
    width: 354px;
    height: 226px;
    overflow: hidden;
  }
  .card--front {
    left: 238px;
    background: var(--gray);
    clip-path: polygon(0 0, 100% 0, 100% 70%, 92% 100%, 0 100%);
  }
  .card--back {
    left: 610px;
    background: var(--blue);
    clip-path: polygon(0 0, 100% 0, 100% 100%, 8% 100%, 0 87%);
  }
  .card__decor {
    position: absolute;
    left: 0; right: 0; bottom: 0;
    height: 66px;
  }
  .card--front .card__decor {
    background: linear-gradient(180deg, var(--gray) 0%, var(--lime) 35%, var(--blue) 75%);
  }
  .card--back .card__decor {
    background: linear-gradient(180deg, var(--blue) 0%, var(--lime) 70%);
  }

  .brand {
    position: absolute;
    left: 0; width: 354px;
    top: 40px;
    text-align: center;
  }
  .brand__dot {
    display: block;
    width: 48px; height: 48px;
    margin: 0 auto 24px;
    border-radius: 50%;
    background: var(--blue);
  }
  .brand__name {
    display: block;
    color: var(--lime);
    font-weight: 700;
    font-size: 20px;
    letter-spacing: 0.5px;
    line-height: 1;
  }
  .brand__region {
    display: block;
    color: var(--lime);
    font-weight: 400;
    font-size: 16px;
    letter-spacing: 0.5px;
    margin-top: 5px;
  }

  .person {
    position: absolute;
    left: 0; width: 304px;
    top: 16px;
    text-align: center;
    color: var(--white);
  }
  .person__name { font-size: 23px; font-weight: 400; line-height: 1.2; }
  .person__role { font-size: 11px; letter-spacing: 0.5px; margin-top: 1px; }

  .contact {
    position: absolute;
    left: 96px; top: 70px;
    list-style: none;
    color: var(--white);
    font-size: 11.5px;
  }
  .contact::before {
    content: "";
    position: absolute;
    left: 26px; top: 0;
    width: 1px; height: 68px;
    background: var(--white);
  }
  .contact__item {
    display: flex;
    align-items: center;
    height: 22px;
  }
  .contact__icon { width: 14px; height: 14px; margin-right: 22px; }
  .contact__icon * { fill: var(--lime); }
</style>
</head>
<body>

<section class="card card--front" aria-label="Card front">
  <div class="card__decor" role="img" aria-label="Angled lime and blue stripe decoration"></div>
  <div class="brand">
    <span class="brand__dot"></span>
    <span class="brand__name">TALL PINE</span>
    <span class="brand__region">HONG KONG</span>
  </div>
</section>

<section class="card card--back" aria-label="Card back">
  <div class="card__decor" role="img" aria-label="Angled lime and blue stripe decoration"></div>
  <div class="person">
    <p class="person__name">Marek Volden</p>
    <p class="person__role">DESIGNER</p>
  </div>
  <ul class="contact">
    <li class="contact__item">
      <svg class="contact__icon" viewBox="0 0 14 14" aria-hidden="true"><path d="M4 1h6a1 1 0 0 1 1 1v10a1 1 0 0 1-1 1H4a1 1 0 0 1-1-1V2a1 1 0 0 1 1-1zm1 2v6h4V3z"/></svg>
      + 852 410 772
    </li>
    <li class="contact__item">
      <svg class="contact__icon" viewBox="0 0 14 14" aria-hidden="true"><path d="M1 3h12v8H1zm1.5 1.2L7 7.5l4.5-3.3V10h-9z"/></svg>
      info@tallpine.com
    </li>
    <li class="contact__item">
      <svg class="contact__icon" viewBox="0 0 14 14" aria-hidden="true"><path d="M7 1a6 6 0 1 1 0 12A6 6 0 0 1 7 1zm0 1.5a4.5 4.5 0 1 0 0 9 4.5 4.5 0 0 0 0-9zM2.5 6.4h9v1.2h-9z"/></svg>
      www.tallpine.com
    </li>
  </ul>
</section>

</body>
</html>
```